Website Re-Design

We would like to explore the possibility of a re-design of our website. We want all the content that it currently has to remain on the pages, and we don't want our logo/corporate identity or colours changed, so it is literally just a website re-design.

Our website is www.drelvix.co.uk

Websites that we like are

http://www.tarnwillow.co.uk/
http://quomplet.com/

```html
<!DOCTYPE html>
<html lang="en">
<head>
<meta charset="utf-8">
<title>Drelvix – Inbound Marketing &amp; SEO Performance Agency</title>
<link href="https://fonts.googleapis.com/css2?family=Open+Sans:wght@300;400;600;700;800&display=swap" rel="stylesheet">
<style>
:root{
  --pink:#e0197d;
  --pink-dark:#b0125f;
  --magenta:#c4166f;
  --ink:#333;
  --text:#666;
  --muted:#999;
  --light:#f2f2f2;
  --dark:#2b2b2b;
  --darker:#1f1f1f;
  --white:#fff;
  --client:#5a8f2e;
  --client-dot:#9bc44b;
  --phone:#1a9fd9;
}
*{box-sizing:border-box;margin:0;padding:0}
html,body{width:1200px;height:2352px;overflow:hidden}
body{font-family:"Open Sans",Arial,sans-serif;color:var(--text);background:var(--white);position:relative}
.wrap{width:960px;margin:0 auto;position:relative}

/* header */
.site-header{height:140px;background:var(--white);position:relative}
.topline{position:absolute;top:10px;left:120px;font-size:13px;color:var(--muted);display:flex;gap:28px}
.topline span::before{content:"";display:inline-block;width:9px;height:9px;border-radius:50%;background:var(--pink);margin-right:7px;vertical-align:middle}
.brand{position:absolute;top:54px;left:120px;font-size:44px;font-weight:800;color:var(--pink);letter-spacing:1px}
.main-nav{position:absolute;top:58px;right:120px;display:flex;background:var(--dark)}
.main-nav a{display:block;padding:16px 22px;font-size:14px;font-weight:600;color:var(--white);text-decoration:none;text-transform:uppercase}
.main-nav a.active{background:var(--pink)}

/* hero */
.hero{height:540px;background:radial-gradient(ellipse at 50% 40%,#e23a8f 0%,var(--magenta) 55%,#8f0e50 100%);position:relative;overflow:hidden}
.hero-art{position:absolute;border-radius:8px}
.hero-art.tree{left:80px;top:24px;width:270px;height:490px;background:linear-gradient(180deg,#45b6a8 0%,#7fb24a 55%,#5b4a3a 100%);opacity:.55}
.hero-art.mailbox{left:830px;top:10px;width:240px;height:500px;background:linear-gradient(180deg,#4fb0c6 0%,#3f8fa5 45%,#7a1347 100%);opacity:.55}
.hero-title{position:absolute;left:360px;top:138px;width:460px;text-align:center;color:var(--white)}
.hero-title h1{font-size:34px;font-weight:700;text-transform:uppercase;line-height:1.15}
.hero-title .band{display:inline-block;margin-top:14px;padding:8px 22px;background:rgba(0,0,0,.22);font-size:24px;font-weight:400;text-transform:uppercase}
.hero-btn{position:absolute;left:545px;top:326px;width:110px;height:40px;border:2px solid var(--white);color:var(--white);font-size:13px;font-weight:600;display:flex;align-items:center;justify-content:center}
.dots{position:absolute;top:460px;left:0;right:0;display:flex;justify-content:center;gap:12px}
.dots i{width:12px;height:12px;border-radius:50%;background:rgba(255,255,255,.5)}
.dots i:first-child{background:var(--white)}

/* intro */
.intro{text-align:center;padding-top:54px}
.intro h2{font-size:30px;font-weight:400;color:var(--ink)}
.intro h2 b{color:var(--pink);font-weight:700}
.intro .lead{margin:26px auto 0;width:820px;font-size:15px;line-height:1.6;color:var(--text)}

.features{display:flex;justify-content:space-between;margin-top:44px}
.feature{width:290px;text-align:center}
.feature svg{display:block;margin:0 auto 16px}
.feature h3{font-size:15px;font-weight:700;color:var(--ink);text-transform:uppercase}
.feature p{width:auto;font-size:13px;line-height:1.5;margin:8px 20px 0;color:var(--muted);white-space:normal}
.btn-dark{display:inline-block;margin-top:16px;padding:9px 30px;background:var(--dark);color:var(--white);font-size:13px}

/* recent works */
.section-title{font-size:32px;font-weight:400;color:var(--ink)}
.works{margin-top:40px}
.work-row{display:flex;justify-content:space-between;margin-top:26px;position:relative}
.work{width:226px}
.work .thumb{height:160px;background:linear-gradient(180deg,#e9e9e9,#c9c9c9);border:1px solid #ddd}
.work h4{margin-top:10px;font-size:12px;font-weight:700;color:var(--ink);text-transform:uppercase;text-align:center;line-height:1.3}
.work p{font-size:11px;color:var(--muted);text-align:center;margin-top:4px}
.arrow{position:absolute;top:62px;width:22px;height:36px;background:var(--dark);display:flex;align-items:center;justify-content:center}
.arrow.prev{left:-30px}.arrow.next{right:-30px}

/* callout */
.callout{margin-top:50px;height:180px;background:var(--light);position:relative}
.callout .box{position:absolute;left:120px;top:24px;width:960px;height:132px;background:var(--white);border-left:6px solid var(--pink);padding:22px 30px}
.callout h3{font-size:26px;font-weight:400;color:var(--ink)}
.callout p{font-size:14px;margin-top:10px;width:600px;line-height:1.5}
.btn-pink{position:absolute;right:40px;top:48px;padding:11px 30px;background:var(--pink);color:var(--white);font-size:15px}

/* clients */
.clients-head{margin-top:40px}
.clients{margin-top:24px;height:200px;background:var(--light)}
.client-row{display:flex;justify-content:space-between;align-items:center;height:200px}
.client{width:180px;display:flex;align-items:center;justify-content:center;gap:10px;font-size:20px;font-weight:700;color:var(--client)}
.client::before{content:"";width:26px;height:26px;border-radius:50%;background:var(--client-dot)}

/* footer */
.site-footer{position:absolute;top:2040px;left:0;width:1200px;height:312px;background:var(--dark);color:#aaa}
.foot-cols{display:flex;padding-top:32px}
.foot-col h5{font-size:17px;font-weight:600;color:var(--white);margin-bottom:14px}
.foot-col p,.foot-col li{font-size:12px;line-height:1.6}
.foot-col ul{list-style:none}
.foot-col li::before{content:"› ";color:var(--pink)}
.col-about{width:320px;padding-right:30px}
.col-menu{width:240px}
.col-where{width:180px;padding-right:10px}
.col-blog{width:220px}
.col-blog h5 b{font-weight:800}
.post{display:flex;gap:10px;margin-bottom:12px}
.post i{width:36px;height:36px;background:#444;flex:none}
.bottom-bar{position:absolute;bottom:0;left:0;width:1200px;height:40px;background:var(--darker)}
.bottom-bar .wrap{display:flex;justify-content:space-between;align-items:center;height:40px;font-size:11px}
.social{display:flex;gap:12px}
.social i{width:20px;height:20px;border-radius:50%;background:#666}
</style>
</head>
<body>

<header class="site-header">
  <div class="topline"><span>+44 (0) 20 7946 0321</span><span>hello@drelvix.co.uk</span></div>
  <div class="brand">DRELVIX</div>
  <nav class="main-nav">
    <a class="active" href="#">Home</a><a href="#">About</a><a href="#">Portfolio</a><a href="#">What we do</a><a href="#">Contact us</a>
  </nav>
</header>

<section class="hero">
  <div class="hero-art tree" role="img" aria-label="Illustration of a stylised tree with coloured circular leaves"></div>
  <div class="hero-art mailbox" role="img" aria-label="Illustration of a teal mailbox with letters"></div>
  <div class="hero-title">
    <h1>Drelvix takes a holistic view</h1>
    <span class="band">of earning your customers attention</span>
  </div>
  <div class="hero-btn">TALK TO US</div>
  <div class="dots"><i></i><i></i><i></i><i></i><i></i></div>
</section>

<section class="wrap intro">
  <h2><b>Drelvix</b> - your inbound marketing &amp; SEO performance agency</h2>
  <p class="lead">Do you want to earn your customers attention? Gain more visibility in the SERPs and build and engage with your audience? Drelvix specialises in SEO, Social media, ERO and Design &amp; Creative services. Offering a bespoke and personal service from a team of digital natives.</p>

  <div class="features">
    <div class="feature">
      <svg width="120" height="90" viewBox="0 0 120 90"><rect x="10" y="30" width="100" height="50" fill="#d9d9d9"/><path d="M10 30 L60 5 L110 30Z" fill="#bdbdbd"/><rect x="30" y="42" width="60" height="26" fill="#fff"/></svg>
      <h3>What can we do for you?</h3>
      <p>We offer a bespoke content and well customised service. We specialise in progressive inbound solutions.</p>
      <span class="btn-dark">Read More</span>
    </div>
    <div class="feature">
      <svg width="120" height="90" viewBox="0 0 120 90"><rect x="30" y="6" width="60" height="80" rx="3" fill="#e0197d"/><rect x="36" y="12" width="48" height="68" fill="#c4166f"/><rect x="42" y="22" width="36" height="6" fill="#fff"/></svg>
      <h3>See our portfolio</h3>
      <p>Take a look at our case studies to see our latest campaigns and the results they delivered.</p>
      <span class="btn-dark">Read More</span>
    </div>
    <div class="feature">
      <svg width="120" height="90" viewBox="0 0 120 90"><circle cx="60" cy="45" r="40" fill="none" stroke="#1a9fd9" stroke-width="5"/><path d="M46 28 q-6 4 0 16 q8 14 20 20 q10 4 14 -2 l-8 -8 q-4 4 -8 0 q-8 -6 -10 -12 q-2 -4 2 -6z" fill="#1a9fd9"/></svg>
      <h3>Let's talk</h3>
      <p>Use our friendly contact form to send a message, we will call you back as soon as we can.</p>
      <span class="btn-dark">Read More</span>
    </div>
  </div>
</section>

<section class="wrap works">
  <h2 class="section-title">Recent Works</h2>
  <div class="work-row">
    <span class="arrow prev"><svg width="10" height="14"><path d="M8 1 L2 7 L8 13" stroke="#fff" stroke-width="2" fill="none"/></svg></span>
    <div class="work"><div class="thumb" role="img" aria-label="Screenshot of a retail website project"></div><h4>Budget Basket Retail Site<br>Waypoint</h4><p>Branding &amp; PR, SEO, Social</p></div>
    <div class="work"><div class="thumb" role="img" aria-label="Screenshot of an infographic project"></div><h4>Infographics – Waypoint</h4><p>SEO, Social</p></div>
    <div class="work"><div class="thumb" role="img" aria-label="Screenshot of a family holiday website"></div><h4>Family Holiday Guide</h4><p>Branding &amp; PR, SEO, Social, Outreach</p></div>
    <div class="work"><div class="thumb" role="img" aria-label="Screenshot of a social guest posts campaign"></div><h4>Social Guests – Waypoint</h4><p>Social</p></div>
    <span class="arrow next"><svg width="10" height="14"><path d="M2 1 L8 7 L2 13" stroke="#fff" stroke-width="2" fill="none"/></svg></span>
  </div>
</section>

<section class="callout">
  <div class="box">
    <h3>Interested in what you have seen so far?</h3>
    <p>Are you looking for a progressive and innovative inbound marketing agency who can work alongside your existing teams? If yes, then let's have a chat.</p>
    <span class="btn-pink">Contact us</span>
  </div>
</section>

<section class="wrap clients-head"><h2 class="section-title">Our Clients</h2></section>
<section class="clients">
  <div class="wrap client-row">
    <div class="client">Fernoak</div>
    <div class="client">Waypoint</div>
    <div class="client">Staywell</div>
    <div class="client">Fernoak</div>
    <div class="client">Waypoint</div>
  </div>
</section>

<footer class="site-footer">
  <div class="wrap foot-cols">
    <div class="foot-col col-about">
      <h5>Drelvix About</h5>
      <p>Drelvix is an inbound marketing agency offering a suite of services from digital strategy and planning through to SEO, Social media, Online PR, Outreach and Design, through to paid media for performance campaigns.</p>
      <p style="margin-top:12px">Phone: +44 (0) 20 7946 0321<br>Address: 14 Harrow Lane, London, UK, W2 5RT</p>
    </div>
    <div class="foot-col col-menu">
      <h5>Main Menu</h5>
      <ul><li>Home</li><li>Blog</li><li>About</li><li>Portfolio</li><li>What we do</li><li>Contact</li></ul>
    </div>
    <div class="foot-col col-where">
      <h5>WHERE ARE WE?</h5>
      <p>We are in London, UK, based down the back streets in a little terrace, so come have a chat with the people who will be more than happy to welcome you in.</p>
    </div>
    <div class="foot-col col-blog">
      <h5>from the <b>BLOG</b></h5>
      <div class="post"><i></i><p>Latest post title here, amet consectetur</p></div>
      <div class="post"><i></i><p>Latest post title here, amet consectetur</p></div>
    </div>
  </div>
  <div class="bottom-bar">
    <div class="wrap">
      <span>© Copyright 2013 Drelvix. All Rights Reserved. | Privacy Policy</span>
      <span class="social"><i></i><i></i><i></i><i></i></span>
    </div>
  </div>
</footer>

</body>
</html>
```